Business website cyber security

Full redesign of our current business website, mockup and powerpoint presentation have been provided.
Some animated elements (example: SVG with CSS) are welcome.
A detailed requirement list can also be found in the attached powerpoint
Also uploaded is the current page as a nicepage & html export. All 11 sites shall be reworked. "Branches", "Download", "Contact" and "Legal Information" are not needed .

A good example of a competitor is https://www.brantvolo.de/ this. Not in terms of colors, but in regard to website structure, animated elements and overall look.

Target Market(s)

Cyber security for the B2B market

Industry/Entity Type

IT, IT Security, banking

Coding

Coded - Design and coding required

Number of Pages Required

5+ page

Font styles to use
Other font styles liked:
• ReadexPro Regular, ReadexPro Light

Colors
0054AA
0677BA
7BADD7
CADEEF
E8F1F8

Requirements
Must have
• Modern and sleek design, corporate identity
Nice to have
• Animated elements (css svg)
Should not have
• too many colors (max 4), too fancy

```html
<!DOCTYPE html>
<html lang="en">
<head>
<meta charset="utf-8">
<title>Corvane – IT Security &amp; Compliance</title>
<link href="https://fonts.googleapis.com/css2?family=Roboto:wght@400;500;700;900&family=Open+Sans:wght@400;600&display=swap" rel="stylesheet">
<style>
:root{
  --navy-900:#020b1a;
  --navy-800:#04152e;
  --navy-700:#0a2345;
  --blue-500:#2391d8;
  --blue-400:#3aa3e6;
  --blue-brand:#0054aa;
  --white:#ffffff;
  --muted:#b9c8da;
  --ink:#1a2433;
}
*{box-sizing:border-box;margin:0;padding:0}
html,body{width:1200px;height:4500px;overflow:hidden}
body{background:var(--navy-800);color:var(--white);font-family:"Open Sans",sans-serif;position:relative}
section,header,footer{position:absolute;left:0;width:1200px}

/* header */
.site-header{top:0;height:88px;background:#161a20;z-index:5}
.brand{position:absolute;left:173px;display:flex;align-items:center;gap:10px;font-family:"Roboto",sans-serif;font-weight:700;font-size:26px;color:var(--white);white-space:nowrap}
.brand i{display:block;width:16px;height:16px;border-radius:50%;background:var(--blue-500)}
.site-header .brand{top:27px}
.nav{position:absolute;top:38px;font-family:"Roboto",sans-serif;font-size:13px;color:#dfe6ee;white-space:nowrap}
.nav-left{left:358px;display:flex;gap:34px}
.nav-right{left:740px;display:flex;gap:28px}
.lang{position:absolute;left:997px;top:22px;width:30px;height:46px;background:#4a5058;font-size:10px;text-align:center;line-height:14px;padding-top:9px;color:#fff}

/* hero */
.hero{top:88px;height:640px;overflow:hidden}
.hero-bg{position:absolute;inset:0;background:radial-gradient(ellipse at 72% 32%,#1b4d7a 0%,#0b2a4c 35%,#061a33 70%),linear-gradient(180deg,#0d2a47,#04152e)}
.hero-bg::after{content:"";position:absolute;left:0;right:0;bottom:0;height:220px;background:linear-gradient(180deg,transparent,var(--navy-800))}
.hero-title{position:absolute;left:173px;top:108px;font-family:"Roboto",sans-serif;font-weight:900;font-size:37px;line-height:51px;text-transform:uppercase;white-space:nowrap}
.hero-copy{position:absolute;left:173px;top:320px;width:330px;font-size:13.5px;line-height:24px;color:#e6edf5}
.hero-name{position:absolute;left:600px;top:200px;width:400px;text-align:center;font-family:"Roboto",sans-serif;font-weight:700;font-size:84px;color:var(--blue-500)}
.hero-tag{position:absolute;left:600px;top:322px;width:400px;text-align:center;font-family:"Roboto",sans-serif;font-weight:500;font-size:22px;color:var(--white)}
.contact-bubble{position:absolute;left:944px;top:342px;width:212px;height:112px;background:var(--blue-500);border-radius:10px;padding:22px 14px;font-size:13px;line-height:33px;white-space:nowrap}
.contact-bubble::after{content:"";position:absolute;right:32px;bottom:-14px;border-left:16px solid transparent;border-top:16px solid var(--blue-500)}
.contact-bubble svg{vertical-align:-2px;margin-right:8px}
.side-tab{position:absolute;right:0;top:430px;width:40px;height:142px;background:var(--blue-500);border-radius:8px 0 0 8px;z-index:4;display:flex;align-items:center;justify-content:center}
.side-tab span{transform:rotate(-90deg);white-space:nowrap;font-family:"Roboto",sans-serif;font-weight:700;font-size:12px}
.down{position:absolute;left:574px;top:548px;width:52px;height:52px;border-radius:50%;background:var(--white);display:flex;align-items:center;justify-content:center}

/* services */
.services{top:728px;height:380px}
.vline{position:absolute;left:174px;top:0;width:3px;height:78px;background:var(--blue-500)}
.cards{position:absolute;left:173px;top:112px;display:flex;gap:28px}
.card{width:267px;height:222px;background:var(--blue-500);border-radius:8px;padding:14px 20px}
.card svg{display:block;margin-bottom:12px}
.card h3{font-family:"Roboto",sans-serif;font-weight:700;font-size:19px;line-height:23px;margin-bottom:10px}
.card p{font-size:13px;line-height:19px}

/* vision */
.vision{top:1108px;height:700px;background:radial-gradient(ellipse at 50% 30%,#0f3563 0%,var(--navy-800) 65%)}
.eyebrow{text-align:center;font-family:"Roboto",sans-serif;font-size:14px;font-weight:500;padding-top:150px;letter-spacing:.5px}
.sec-title{text-align:center;font-family:"Roboto",sans-serif;font-weight:700;font-size:38px;letter-spacing:1px;margin-top:10px}
.tabs{position:absolute;left:173px;top:260px;width:182px}
.tab{height:100px;margin-bottom:24px;background:var(--navy-700);display:flex;align-items:center;justify-content:center;font-family:"Roboto",sans-serif;font-weight:700;font-size:16px;letter-spacing:.5px}
.tab.active{background:var(--blue-500);border-radius:4px}
.tab-panel{position:absolute;left:376px;top:260px;width:652px;height:348px;background:var(--white);border-radius:10px;color:var(--ink);padding:36px 56px}
.tab-panel h4{font-family:"Roboto",sans-serif;font-weight:500;font-size:20px;margin-bottom:18px}
.tab-panel p,.tab-panel li{font-size:13.5px;line-height:22px;color:#333}
.tab-panel ul{list-style:none;margin:4px 0}
.tab-panel li{padding-left:15px;position:relative;margin-bottom:6px}
.tab-panel li::before{content:"";position:absolute;left:0;top:7px;width:8px;height:8px;background:var(--blue-500)}

/* industry */
.industry{top:1808px;height:680px}
.ind-title{position:absolute;left:173px;top:190px;font-family:"Roboto",sans-serif;font-weight:900;font-size:38px;line-height:44px;text-transform:uppercase}
.tile{position:absolute;width:272px;height:186px;border-radius:3px}
.tile-label{position:absolute;font-family:"Roboto",sans-serif;font-weight:700;font-size:15px}
.fin{background:linear-gradient(135deg,#2a9ae0,#1f7fc4);padding:18px 10px;font-size:13.5px;line-height:25px}
.fin strong{font-family:"Roboto",sans-serif;font-size:15px;display:block;letter-spacing:.3px}
.fin div{padding-left:14px;position:relative}
.fin div::before{content:"›";position:absolute;left:0}

/* team */
.team{top:2488px;height:520px}
.illus{position:absolute;left:173px;top:20px;width:496px;height:430px;background:radial-gradient(ellipse at 45% 60%,#7f7ff0 0%,#3a3fae 40%,rgba(4,21,46,0) 72%)}
.quote{position:absolute;left:700px;top:230px;width:330px;text-align:center;font-family:"Roboto",sans-serif;font-weight:500;font-size:20px;line-height:27px}
.btn{position:absolute;left:735px;width:256px;height:38px;display:flex;align-items:center;justify-content:center;font-family:"Roboto",sans-serif;font-weight:500;font-size:14px;letter-spacing:.3px}
.btn-fill{top:312px;background:var(--blue-500)}
.btn-line{top:363px;border:2px solid var(--blue-500)}

/* partners */
.partners{top:3008px;height:530px;background:linear-gradient(180deg,var(--navy-800),#06234a 50%,var(--navy-800))}
.partners .sec-title{padding-top:190px;margin:0}
.sub{text-align:center;font-family:"Roboto",sans-serif;font-weight:500;font-size:15px;margin-top:4px}
.logos{position:absolute;left:173px;width:860px;display:flex;justify-content:space-between;align-items:center;font-family:"Roboto",sans-serif;font-weight:500;font-size:22px;color:#e8eef5}
.logos span{width:160px;text-align:center;display:flex;align-items:center;justify-content:center;gap:8px;white-space:nowrap}
.logos i{display:inline-block;width:14px;height:14px;border-radius:50%;border:2px solid #e8eef5}

/* news */
.news{top:3538px;height:540px}
.news .sec-title{padding-top:180px;margin:0;font-size:36px}
.posts{position:absolute;left:171px;top:265px;display:flex;gap:12px}
.post{width:207px}
.post-img{height:142px}
.post h5{font-family:"Roboto",sans-serif;font-weight:700;font-size:15px;margin:12px 0 4px}
.post p{font-size:13.5px;line-height:22px}
.more{display:inline-block;margin-top:18px;background:var(--blue-500);font-family:"Roboto",sans-serif;font-weight:700;font-size:11px;padding:10px 22px}

/* footer */
.site-footer{top:4078px;height:422px;background:var(--navy-900)}
.site-footer .brand{top:260px}
.foot-info{position:absolute;left:0;width:1200px;text-align:center;top:258px;font-size:13px;color:#e6edf5}
.foot-links{position:absolute;left:0;width:1200px;text-align:center;top:292px;font-size:13px;color:var(--muted)}
.foot-links span{margin:0 12px}
.social{position:absolute;left:987px;top:258px;width:38px;height:38px;border-radius:50%;background:var(--white);display:flex;align-items:center;justify-content:center}
.social i{display:block;width:22px;height:22px;background:var(--blue-brand);border-radius:3px}
.copy{position:absolute;left:0;width:1200px;text-align:center;top:392px;font-size:12px;color:#dfe6ee}
.copy em{font-style:normal;color:var(--blue-400)}
</style>
</head>
<body>

<header class="site-header">
  <div class="brand"><i></i>Corvane</div>
  <nav class="nav nav-left"><span>CDaaS</span><span>Security Services</span><span>Compliance</span></nav>
  <nav class="nav nav-right"><span>Company</span><span>Career</span><span>Contact</span></nav>
  <div class="lang">EN<br>DE</div>
</header>

<section class="hero">
  <div class="hero-bg" role="img" aria-label="Dark blue server room with rows of lit data center racks"></div>
  <h1 class="hero-title">The IT security<br>of your IT<br>infrastructure<br>is our mission</h1>
  <p class="hero-copy">Our cybersecurity services are designed around the customer. We offer a robust collaboration to understand the challenges of your environment and to develop tailor-made, secure solutions.</p>
  <div class="hero-name">Corvane</div>
  <div class="hero-tag">IT - Security - Compliance</div>
  <div class="contact-bubble">
    <div><svg width="14" height="11" viewBox="0 0 14 11"><rect width="14" height="11" rx="1" fill="#fff"/><path d="M0 1l7 5 7-5" stroke="#2391d8" stroke-width="1.5" fill="none"/></svg>info@corvanesecurity.com</div>
    <div><svg width="13" height="13" viewBox="0 0 24 24"><path fill="#fff" d="M6.6 10.8a15 15 0 006.6 6.6l2.2-2.2a1 1 0 011-.25 11.4 11.4 0 003.6.6 1 1 0 011 1V20a1 1 0 01-1 1A17 17 0 013 4a1 1 0 011-1h3.5a1 1 0 011 1c0 1.25.2 2.45.6 3.6a1 1 0 01-.25 1z"/></svg>01 555 010 200</div>
  </div>
  <div class="side-tab"><span>CONTACT US</span></div>
  <div class="down"><svg width="20" height="12" viewBox="0 0 20 12"><path d="M2 2l8 8 8-8" stroke="#0054aa" stroke-width="3" fill="none"/></svg></div>
</section>

<section class="services">
  <div class="vline"></div>
  <div class="cards">
    <article class="card">
      <svg width="44" height="44" viewBox="0 0 44 44"><circle cx="22" cy="22" r="20" fill="none" stroke="#fff" stroke-width="2.5"/><path d="M22 10l9 4v7c0 6-4 10-9 12-5-2-9-6-9-12v-7z" fill="none" stroke="#fff" stroke-width="2.5"/><path d="M17 21l4 4 6-7" stroke="#fff" stroke-width="2.5" fill="none"/></svg>
      <h3>CDaaS - Cyber Defense as a Service</h3>
      <p>Our all-in-one CDaaS offer offers a convenient integration of your IT infrastructure into an active and comprehensive security solution.</p>
    </article>
    <article class="card">
      <svg width="44" height="44" viewBox="0 0 44 44"><path d="M22 3l12 5v10c0 9-6 14-12 17-6-3-12-8-12-17V8z" fill="none" stroke="#fff" stroke-width="2.5"/><path d="M16 18l5 5 8-9" stroke="#fff" stroke-width="2.5" fill="none"/><path d="M4 36c6 0 8 5 18 5s14-3 18-6" stroke="#fff" stroke-width="2.5" fill="none"/></svg>
      <h3>Security Services</h3>
      <p>Our security services provide you with comprehensive support in the planning and implementation of your holistic IT and information management.</p>
    </article>
    <article class="card">
      <svg width="44" height="44" viewBox="0 0 44 44"><rect x="6" y="5" width="24" height="32" rx="2" fill="none" stroke="#fff" stroke-width="2.5"/><rect x="13" y="2" width="10" height="6" fill="#fff"/><path d="M11 15h3M17 15h9M11 22h3M17 22h9M11 29h3M17 29h6" stroke="#fff" stroke-width="2.5"/><circle cx="34" cy="34" r="7" fill="#fff"/><path d="M31 34l2 2 4-4" stroke="#2391d8" stroke-width="2" fill="none"/></svg>
      <h3>Compliance</h3>
      <p>We support you with your IT security at the highest level with an effective compliance strategy.</p>
    </article>
  </div>
</section>

<section class="vision">
  <p class="eyebrow">HENCE THE CORVANE SÀRL</p>
  <h2 class="sec-title">VISION &amp; MISSION</h2>
  <div class="tabs">
    <div class="tab active">VISION</div>
    <div class="tab">MISSION</div>
    <div class="tab">PORTFOLIO</div>
  </div>
  <div class="tab-panel">
    <h4>Holistic IT security is our claim</h4>
    <p>We stand for your IT security. We offer extensive services and our certified IT experts work with you to ensure that your systems are secure.</p>
    <p>With us you have:</p>
    <ul><li>Fastest response times 24x7</li><li>Market</li></ul>
    <p>&nbsp;leading technologies • Certified cyber analysts with the highest level of expertise</p>
    <p>The "Pay-As-You-Grow" model allows ongoing adjustments to the professional security services used - with one claim: your needs.</p>
  </div>
</section>

<section class="industry">
  <h2 class="ind-title">Industry<br>sectors</h2>
  <div class="tile fin" style="left:464px;top:150px">
    <strong>FINANCIAL SECTOR</strong>
    <div>Fund Management</div><div>Core banking systems</div><div>Trading systems</div><div style="line-height:18px;margin-top:4px">Reporting systems (FINREP, COREP, Ledgera Suite)</div>
  </div>
  <div class="tile" style="left:756px;top:150px;background:linear-gradient(135deg,#1c3554,#5d7da0 60%,#d9dde3)" role="img" aria-label="Hands using a tablet with floating data charts"></div>
  <div class="tile-label" style="left:756px;top:348px">IT SERVICE OPS</div>
  <div class="tile" style="left:173px;top:400px;background:linear-gradient(135deg,#1a2a3d,#4f6f8f 50%,#c9762e)" role="img" aria-label="Robotic arms on an automotive assembly line"></div>
  <div class="tile-label" style="left:173px;top:598px">AUTOMOBIL INDUSTRIE</div>
  <div class="tile" style="left:464px;top:400px;background:linear-gradient(180deg,#5f9fd9,#c8e0f2 45%,#3a6fb0 60%,#4c7a3a)" role="img" aria-label="Solar panels and wind turbines under a blue sky"></div>
  <div class="tile-label" style="left:464px;top:598px">ENERGY</div>
  <div class="tile" style="left:756px;top:400px;background:linear-gradient(180deg,#e59a4e,#b77a52 45%,#3e4c5c)" role="img" aria-label="Truck and shipping containers at a logistics yard at sunset"></div>
  <div class="tile-label" style="left:756px;top:598px">LOGISTICS</div>
</section>

<section class="team">
  <div class="illus" role="img" aria-label="Illustration of two business people shaking hands on a paper plane"></div>
  <p class="quote">"We rely on trust, reliability and professionalism"</p>
  <div class="btn btn-fill">BECOME PART OF THE TEAM!</div>
  <div class="btn btn-line">WORKING AT CORVANE</div>
</section>

<section class="partners">
  <h2 class="sec-title">PRODUCTS &amp; PARTNERS</h2>
  <p class="sub">We will find the best solution for you. We develop a wide range of services with our individual solutions</p>
  <div class="logos" style="top:330px">
    <span><i></i>Aulvix</span><span>Merivon</span><span>Tessaro Cloud</span><span>Nubrik</span><span>Veltaro</span>
  </div>
  <div class="logos" style="top:450px">
    <span>Quorra</span><span>Hexlane</span><span>Pyrolin</span><span>Kelmsec</span><span>Strondyx</span>
  </div>
</section>

<section class="news">
  <h2 class="sec-title">LATEST NEWS</h2>
  <div class="posts">
    <article class="post"><div class="post-img" role="img" aria-label="Glowing blue padlock on a digital circuit ring" style="background:radial-gradient(circle,#5fb4f0,#0b3a78 70%)"></div><h5>POST 6 HEADLINE</h5><p>Example small text. Lorem ipsum dolor sit amet</p><span class="more">READ MORE ▸</span></article>
    <article class="post"><div class="post-img" role="img" aria-label="Hand touching a shield icon on a transparent screen" style="background:linear-gradient(135deg,#e6e8ec,#8b939e)"></div><h5>POST 6 HEADLINE</h5><p>Example small text. Lorem ipsum dolor sit amet</p><span class="more">READ MORE ▸</span></article>
    <article class="post"><div class="post-img" role="img" aria-label="Analysts working at monitors in a security operations center" style="background:linear-gradient(135deg,#1d2c44,#5a7fa8)"></div><h5>POST 6 HEADLINE</h5><p>Example small text. Lorem ipsum dolor sit amet</p><span class="more">READ MORE ▸</span></article>
    <article class="post"><div class="post-img" role="img" aria-label="Business person in a dark suit holding a drone" style="background:linear-gradient(135deg,#0c0c10,#3a3d44)"></div><h5>POST 6 HEADLINE</h5><p>Example small text. Lorem ipsum dolor sit amet</p><span class="more">READ MORE ▸</span></article>
  </div>
</section>

<footer class="site-footer">
  <div class="brand"><i></i>Corvane</div>
  <p class="foot-info">© Corvane (S.à rl) • Tel.: +352 5550 10 20 - 30</p>
  <p class="foot-links"><span>Contact</span>•<span>Imprint</span>•<span>Privacy</span>•<span>Legal Notice</span></p>
  <div class="social"><i></i></div>
  <p class="copy">© 2022 <em>Corvane IT Security Compliance</em> All right reserved</p>
</footer>

</body>
</html>
```